Sale- Bundle signs

We are looking for a design to use for Permanent SALE/Bundle deal signs. We are a natural bath products company who uses all natural ingredients to create our handmade line of natural products. We love a clean, fresh look and feel. Simple eye-catching that will be a quick glance and they will know the offer.
We would like to have something simple, eye catching that will promote sales on our different products.
Dead Sea Salt Body Scrubs
large 2 for $40
small 3 for $20
Moisturizing Wash with coconut & olive oil
2 for $20
There are several more needed but we are hoping to decide on one template before making all of the signs.
Visit our website here www.bramblecovewash.com
Target Market(s)
Our store serves 70% women and the majority of our customers are 30+ years old.
Industry/Entity Type
It Company
Font styles to use
Other font styles liked:
- Century Gothic or similar

```html
<!DOCTYPE html>
<html lang="en">
<head>
<meta charset="UTF-8">
<title>Bramble Cove — Bundle Deals</title>
<link href="https://fonts.googleapis.com/css2?family=Questrial&family=Arimo:wght@400;700&family=Nunito+Sans:wght@800&display=swap" rel="stylesheet">
<style>
  :root {
    --brand-green: #5f8f2c;
    --ink: #1c1a17;
    --offer-orange: #e8781e;
    --sea-blue: #a9c3d3;
    --sea-mist: #eef3f5;
    --cloud: #fbf9f4;
    --sand-light: #f6e6c4;
    --sand: #eed3a0;
  }
  * { margin: 0; padding: 0; box-sizing: border-box; }
  html, body { width: 857px; height: 1200px; overflow: hidden; }
  body { background: var(--cloud); }
  .sign {
    position: relative;
    width: 857px;
    height: 1200px;
    overflow: hidden;
    font-family: "Questrial", "Century Gothic", sans-serif;
    color: var(--ink);
  }
  .sign__backdrop {
    position: absolute;
    inset: 0;
    background:
      radial-gradient(ellipse 60% 30% at 58% 50%, rgba(255,255,255,0.95) 0%, rgba(255,255,255,0) 100%),
      linear-gradient(180deg,
        var(--sea-mist) 0%,
        #d5e2ea 18%,
        var(--sea-blue) 30%,
        #dfe8ec 42%,
        var(--cloud) 52%,
        var(--sand-light) 70%,
        var(--sand) 100%);
  }
  .sign__block { position: absolute; left: 0; width: 100%; text-align: center; }
  .brand { top: 22px; }
  .brand__name {
    font-size: 98px;
    line-height: 1;
    color: var(--brand-green);
    letter-spacing: 1px;
  }
  .brand__tagline {
    margin-top: 6px;
    font-family: "Arimo", sans-serif;
    font-weight: 700;
    font-size: 27px;
    letter-spacing: 0.5px;
    color: var(--brand-green);
  }
  .product-title {
    font-family: "Arimo", sans-serif;
    font-size: 24px;
    text-transform: uppercase;
    letter-spacing: 0.3px;
  }
  .product-title--scrubs { top: 258px; left: 0; }
  .deal {
    position: absolute;
    width: 400px;
    text-align: center;
    line-height: 1;
  }
  .deal--large { left: -10px; top: 370px; }
  .deal--small { left: 445px; top: 392px; }
  .deal__size {
    font-family: "Nunito Sans", sans-serif;
    font-weight: 800;
    font-size: 52px;
    color: var(--ink);
  }
  .deal__price {
    margin-top: 8px;
    font-family: "Arimo", sans-serif;
    font-weight: 700;
    font-size: 80px;
    color: var(--offer-orange);
  }
  .deal--small .deal__price { margin-top: 2px; }
  .product-title--wash {
    top: 730px;
    font-size: 38px;
    line-height: 1.55;
  }
  .wash-price {
    top: 928px;
    font-family: "Arimo", sans-serif;
    font-weight: 700;
    font-size: 128px;
    color: var(--offer-orange);
    line-height: 1;
  }
</style>
</head>
<body>
  <main class="sign">
    <div class="sign__backdrop" role="img" aria-label="Soft photo of a calm blue sea fading into warm golden sand"></div>

    <header class="sign__block brand">
      <div class="brand__name">bramble cove</div>
      <div class="brand__tagline">NATURAL BATH PRODUCTS</div>
    </header>

    <h2 class="sign__block product-title product-title--scrubs">Dead Sea Salt Body Scrubs</h2>

    <section class="deal deal--large">
      <div class="deal__size">Large 2</div>
      <div class="deal__price">for $40</div>
    </section>

    <section class="deal deal--small">
      <div class="deal__size">Small 3</div>
      <div class="deal__price">for $20</div>
    </section>

    <h2 class="sign__block product-title product-title--wash">Moisturizing Wash<br>with<br>Coconut &amp; Olive Oil</h2>

    <div class="sign__block wash-price">2 for $20</div>
  </main>
</body>
</html>
```